依頼詳細
メディアに掲載されている資料を添付します。
シンプルに申しますと、資料を1枚のチラシにまとめたい、というものになります。
BtoBのサービスの為、アポイントを取って商談に伺う必要があるのですが、新規顧客に対してのサービスの大枠の概要を説明するツールとして、チラシを見て興味を惹き、アポイント⇒商談に繋げる目的のものです。
「詳しく話を聞きたい」「確かにうちは何も対策をしていない、しなくては!」と思ってもらえる様なチラシを作りたいです。

キャッチコピー案もいくつか考えてみましたが、完全にしっくりきているわけではないので使用の有無はお任せさせてください。『「爆買い」を呼びこむ決定版!』『「爆買い」を自分で仕掛ける!』『「爆買い」の仕掛け、出来ていますか?』など。
ベースとなるカラーは、「希望する色」内「その他」にて、サービス提供会社のコーポレートカラーをRGB値とHSL値で記載していますが、その他、チラシ内の資料や強調で別の色をお使いいただくなどはお任せさせてください。
「シャープ」「スマート」「価値が高い」というイメージを打ち出したいです。

https://www.hoshinami-link.co.jp/service/
※ページ下部「トラベリオMQT」
記載項目
上記キーワードなどに加え、添付資料からの抜粋をお願いします。
チラシの右下あたりに、以下もご記載ください。
「お問合せはこちらまでお願いします。
○○○○
○○○@kumomail.jp
担当:○○」
サイズ
A4
ページ数
片面
希望イメージ
シンプル 複雑
単色 カラフル
暗い 明るい
日常 高級
遊び心 厳粛
未来的 伝統的
女性的 男性的
希望する色
水色系、RGB値(R:82・G:196・B:197)、HSL値(U:128・S:127・L:140)
納品ファイル
• 高解像度JPG (.jpg)
• イラストレーター形式 (.ai)
補足説明
・サービスが分かりづらいかも知れません。ご不明な点はご質問くださいませ。
納期を14日後の12/25に変更致します。

是非、多くのみなさまからのご提案をいただけたらと思います。
宜しくお願いします。
大変申し訳ございません。

```html
<!DOCTYPE html>
<html lang="ja">
<head>
<meta charset="utf-8">
<title>「爆買い」を呼びこむ決定版!</title>
<link href="https://fonts.googleapis.com/css2?family=Noto+Sans+JP:wght@400;500;700;900&display=swap" rel="stylesheet">
<style>
:root{
  --aqua:#52c4c5;
  --aqua-pale:#dff4f5;
  --aqua-soft:#b9e7e8;
  --navy:#1d3a73;
  --blue:#1f6fb8;
  --red:#e5004f;
  --yellow:#ffe14a;
  --ink:#333;
  --white:#fff;
}
*{margin:0;padding:0;box-sizing:border-box}
html,body{width:869px;height:1200px;overflow:hidden;background:#fff}
body{font-family:"Noto Sans JP",sans-serif;color:var(--ink);position:relative}
.flyer{position:relative;width:869px;height:1200px;overflow:hidden;background:#fff}
.stripes{position:absolute;left:0;top:0;width:520px;height:470px;
  background:repeating-linear-gradient(135deg,var(--aqua-pale) 0 14px,#fff 14px 28px);opacity:.8}
.hero-photo{position:absolute;left:435px;top:0;width:434px;height:470px;
  background:linear-gradient(160deg,#eef7f8 0%,#d5ecee 55%,#b9dfe2 100%)}
.headline{position:absolute;left:40px;top:26px;font-weight:900;color:var(--navy);line-height:1.14}
.headline .hot{display:inline-block;background:var(--red);color:#fff;padding:0 8px;font-size:70px;border-radius:6px;line-height:1.2}
.headline .particle{font-size:62px}
.headline .line{font-size:74px;display:block}
.callout{position:absolute;left:180px;top:298px;width:270px;padding:8px 14px;background:#fff;
  border:3px solid var(--aqua);border-radius:10px;color:var(--blue);font-weight:700;font-size:15px;line-height:1.45}
.intro{position:absolute;left:40px;top:378px;width:600px;font-size:13.5px;line-height:1.6;font-weight:500}
.intro .stat{display:block;margin-top:2px;line-height:1.3}
.intro .big{font-size:24px;font-weight:900;color:var(--red);background:linear-gradient(transparent 60%,var(--yellow) 60%)}
.band{position:absolute;left:0;top:478px;width:869px;height:172px;background:var(--aqua)}
.question{position:absolute;left:28px;top:500px;width:230px;height:128px;background:#fff;border-radius:14px;
  padding:12px 14px;color:var(--red);font-weight:900;font-size:18px;line-height:1.45}
.question::after{content:"";position:absolute;right:-22px;top:52px;border:12px solid transparent;border-left:14px solid #fff}
.points{position:absolute;left:282px;top:500px;width:560px;height:128px;background:#fff;border-radius:10px;
  padding:14px 20px;list-style:none;font-weight:700;font-size:17px;line-height:1.5;color:var(--navy)}
.points li::before{content:"■";color:var(--aqua);margin-right:6px}
.points em{font-style:normal;color:var(--red)}
.partners{position:absolute;left:40px;top:668px;display:flex;align-items:center;gap:8px;font-size:15px;font-weight:700;color:var(--navy);white-space:nowrap}
.partner{display:flex;align-items:center;gap:6px;border:2px solid var(--aqua);border-radius:6px;padding:5px 10px;font-size:14px;color:var(--navy)}
.partner .dot{width:14px;height:14px;background:var(--aqua)}
.partners .service{color:var(--blue);font-size:21px;font-weight:900}
.target{position:absolute;left:40px;top:716px;font-size:32px;font-weight:900;color:var(--navy);white-space:nowrap}
.target em{font-style:normal;color:var(--red)}
.promo{position:absolute;left:0;top:775px;width:869px;height:46px;background:var(--navy);color:#fff;
  display:flex;align-items:center;justify-content:center;font-weight:900;font-size:19px;gap:6px;white-space:nowrap}
.promo em{font-style:normal;color:var(--yellow);font-size:24px}
.about{position:absolute;left:40px;top:836px;width:530px;font-size:12.5px;line-height:1.65}
.about h3{font-size:17px;color:var(--blue);font-weight:900;margin-bottom:4px}
.about-art{position:absolute;left:600px;top:836px;width:230px;height:130px;border-radius:8px;
  background:linear-gradient(135deg,var(--aqua-pale),var(--aqua-soft))}
.contact{position:absolute;left:40px;top:980px;width:790px;height:46px;border:2px solid var(--aqua);border-radius:23px;
  display:flex;align-items:center;padding:0 24px;gap:28px;font-weight:700;font-size:15px;color:var(--navy);white-space:nowrap}
.contact .mail{color:var(--blue)}
.footer{position:absolute;left:0;top:1045px;width:869px;height:155px;background:var(--aqua-pale);border-top:4px solid var(--aqua)}
.brand{position:absolute;left:40px;top:32px;display:flex;align-items:center;gap:10px;font-weight:900;font-size:22px;color:var(--navy);white-space:nowrap}
.brand .mark{width:32px;height:32px;border-radius:50%;background:var(--aqua)}
.company{position:absolute;left:300px;top:30px;font-size:14px;line-height:1.6;font-weight:500;white-space:nowrap}
.company strong{font-size:16px;font-weight:900;color:var(--navy)}
.tel{position:absolute;right:40px;top:30px;text-align:right;font-size:15px;line-height:1.6;font-weight:700;color:var(--navy)}
</style>
</head>
<body>
<div class="flyer">
  <div class="stripes"></div>
  <div class="hero-photo" role="img" aria-label="指差しで呼びかけるビジネススーツの女性の写真"></div>

  <h1 class="headline">
    <span class="hot">「爆買い」</span><span class="particle">を</span>
    <span class="line">呼びこむ</span>
    <span class="line">決定版!!</span>
  </h1>

  <p class="callout">2015年流行語にもなった「爆買い」。インバウンド対策できていますか?</p>

  <p class="intro">海外からのインバウンド客が年々増加しており、特に中国観光客(中国・台湾・香港)の利用者数が全体を牽引。<span class="stat">統計開始の<span class="big">20年度と比較して約4倍</span>この傾向は今後も続く見込み。</span></p>

  <div class="band"></div>
  <p class="question">日本人とは違う、中国人の「旅行の計画」の立て方の特徴、ご存じでしたか?</p>
  <ul class="points">
    <li>中国の人は、「<em>旅行出発前</em>」に「<em>綿密な計画を立てて</em>」「<em>爆買い</em>」する</li>
    <li>「春節」「国慶節」「年末年始」など、年間を通してのプロモーションの必要性</li>
  </ul>

  <div class="partners">
    <span class="partner"><span class="dot"></span>カードパートナー</span>
    <span>と</span>
    <span class="partner"><span class="dot"></span>HOSHINAMI LINK</span>
    <span>が共同で提供するサービス</span>
    <span class="service">「トラベリオMQT」</span><span>で</span>
  </div>
  <p class="target">特に<em>「爆買い」</em>をする<em>「富裕層」</em>にターゲティング</p>

  <div class="promo">これらの施策を<em>「ほぼ成果報酬型」</em>で実施!効率的なプロモーション施策を!</div>

  <div class="about">
    <h3>トラベリオMQT(カードリンク・サービス)とは?</h3>
    <p>高額決済の多い海外カード会員へ、渡航前に店舗の特典情報を届ける仕組みです。会員が来日後に対象店舗でカード決済すると、利用実績に応じて費用が発生するため、無駄のない集客施策を実現します。詳細はサービスページ https://www.hoshinami-link.co.jp/service/ をご覧ください。</p>
  </div>
  <div class="about-art" role="img" aria-label="旅行鞄と飛行機のイラスト"></div>

  <div class="contact">
    <span>お問合せはこちらまでお願いします。</span>
    <span>○○○○</span>
    <span class="mail">○○○@kumomail.jp</span>
    <span>担当:○○</span>
  </div>

  <footer class="footer">
    <div class="brand"><span class="mark"></span>HOSHINAMI LINK</div>
    <p class="company"><strong>ホシナミリンク株式会社</strong><br>東京都港区星浪町2-8-1 ミナトテラス</p>
    <p class="tel">Tel.03-6800-2417<br>www.hoshinami-link.co.jp</p>
  </footer>
</div>
</body>
</html>
```